Website Design for Australian Vocational Education organisation

A website for an Educational organisation. A responsive design that works well on a laptop desktop or a mobile phone. Is easy to navigate. Be able to start small and add new pages and features at a later stage.
Requires the logo, the name of company, home page with hero shots, enquiry form that forwards to a specified email address
links to social media, home page. We need a home page, and two more templates for sub pages.
Must not be a typical common design.

current website www.qvtl.edu.au
this needs to look different. logo should remain the same.

Target Market(s)

across age groups from 18-70. so must be inutitive. some will be tech savvy and others not.

Industry/Entity Type

Education

Coding

Coded - Design and coding required

Colors

Designer to choose colors to be used in the design.

Requirements
Must have
• responsive design, video, photo gallery, hero image, social media links, news feed, calendar, shopping cart, enquiry form
Nice to have
• Sample website
• www.bluegumlearning.com.au
• but should not be similar to this. it must look different. the sample is to give an idea on the various pages and links that will be required

```html
<!DOCTYPE html>
<html lang="en">
<head>
<meta charset="utf-8">
<title>Our Courses – Southern Institute of Applied Skills</title>
<link href="https://fonts.googleapis.com/css2?family=Poppins:wght@400;500;600&display=swap" rel="stylesheet">
<style>
:root{
  --topbar:#0fbcd6;
  --red:#e4232b;
  --nav-home:#e84c3d;
  --nav-about:#f08a2a;
  --nav-courses:#f1c40f;
  --nav-students:#1bb99a;
  --nav-contact:#9b59b6;
  --teal:#19a9ae;
  --text:#222;
  --muted:#666;
  --card:#f6f6f6;
  --navy:#27496a;
  --navy-deep:#2d5a80;
  --white:#fff;
}
*{box-sizing:border-box;margin:0;padding:0}
html,body{width:708px;height:1200px;overflow:hidden}
body{position:relative;background:var(--white);font-family:'Poppins',sans-serif;color:var(--text)}
.abs{position:absolute}

/* top bar */
.topbar{left:0;top:0;width:708px;height:20px;background:var(--topbar);color:var(--white);font-size:5.5px}
.topbar .org{left:139px;top:6.5px}
.topbar .cart{left:352px;top:6.5px}
.topbar .sign{left:412px;top:6.5px}
.social-dot{width:8px;height:8px;border-radius:50%;background:var(--white)}
.enquiry{left:510px;top:2px;width:60px;height:16px;border-radius:8px;background:var(--red);color:var(--white);font-size:5.5px;font-weight:500;display:flex;align-items:center;justify-content:center}

/* header */
.brand{left:139px;top:26px;display:flex;align-items:center;gap:4px}
.brand-mark{width:26px;height:26px;background:var(--navy)}
.brand-name{font-size:6px;font-weight:600;line-height:7px;color:var(--red);text-transform:uppercase}
.nav{left:257px;top:20px;display:flex}
.nav-item{width:62.6px;height:38px;color:var(--white);font-size:5px;font-weight:600;display:flex;flex-direction:column;align-items:center;justify-content:center;gap:3px}
.nav-item i{display:block;width:7px;height:7px;background:var(--white);border-radius:1px}

/* hero */
.hero{left:0;top:58px;width:708px;height:126px;background:linear-gradient(100deg,#3a3a3c 0%,#6b5a4e 35%,#8a7a6a 60%,#4a4746 100%)}
.hero-title{left:0;top:108px;width:708px;text-align:center;color:var(--white);font-size:19px;font-weight:600}
.crumb{left:0;top:137px;width:708px;text-align:center;color:var(--white);font-size:5.8px}

/* courses */
.card{width:136px;height:208px;background:var(--card)}
.card .photo{width:136px;height:100px}
.card .cat{position:absolute;left:9px;top:109px;font-size:4.8px;color:var(--teal);text-transform:uppercase}
.card .title{position:absolute;left:9px;top:117px;width:125px;font-size:7.3px;font-weight:600;line-height:9px;color:var(--teal);text-transform:uppercase}
.card .meta{position:absolute;left:9px;top:142px;font-size:5.5px;color:var(--muted);display:flex;align-items:center;gap:3px}
.card .meta b{display:inline-block;width:5px;height:5px;background:#888}
.card .meta s{display:inline-block;width:5px;height:5px;border:1px solid #666;border-radius:50%;margin-left:4px}
.card .desc{position:absolute;left:9px;top:153px;width:120px;font-size:5.3px;line-height:8.8px;color:var(--text)}
.card .apply{position:absolute;left:44px;top:185px;width:48px;height:12px;border-radius:6px;background:var(--red);color:var(--white);font-size:5px;font-weight:500;display:flex;align-items:center;justify-content:center}

.load-more{left:321px;top:907px;width:67px;height:16px;border:1px solid var(--nav-contact);color:var(--nav-contact);font-size:6.5px;font-weight:500;display:flex;align-items:center;justify-content:center}

/* footer */
.footer-bg{left:0;top:922px;width:708px;height:246px}
.footer-badge{left:333px;top:957px;width:45px;height:45px;border-radius:50%;background:var(--white);display:flex;align-items:center;justify-content:center;font-size:7px;font-weight:600;color:var(--navy)}
.f-brand{left:139px;top:1026px;display:flex;align-items:center;gap:4px}
.f-brand .brand-mark{background:var(--white)}
.f-brand .brand-name{color:var(--white)}
.f-contact{left:139px;font-size:5.3px;color:var(--white);display:flex;gap:6px;line-height:8px}
.f-contact i{display:block;width:7px;height:7px;border:1px solid var(--white);border-radius:50%;flex:none;margin-top:1px}
.f-head{font-size:6.5px;font-weight:500;color:var(--white)}
.f-head::after{content:"";display:block;width:15px;height:1px;background:var(--red);margin-top:5px}
.f-list{list-style:none;font-size:5.3px;color:var(--white)}
.f-list li{height:14.8px}
.f-list li::before{content:"›";margin-right:4px}
.f-news{left:449px;top:1027px;width:124px;font-size:6.3px;line-height:9px;color:var(--white)}
.f-input{left:449px;top:1048px;width:119px;height:20px;background:var(--white);font-size:5.3px;color:#777;padding-left:7px;display:flex;align-items:center}
.f-social{width:13px;height:13px;border-radius:50%;border:1px solid var(--white)}
.copyright{left:0;top:1168px;width:708px;height:32px;background:var(--navy-deep);color:var(--white);font-size:6px;display:flex;align-items:center;justify-content:center}
</style>
</head>
<body>

<header>
  <div class="abs topbar">
    <span class="abs org">Southern Institute of Applied Skills (SIAS)</span>
    <span class="abs cart">🛒 Shopping Cart</span>
    <span class="abs sign">Sign In / Register</span>
    <span class="abs social-dot" style="left:465px;top:6px"></span>
    <span class="abs social-dot" style="left:478px;top:6px"></span>
    <span class="abs social-dot" style="left:491px;top:6px"></span>
    <span class="abs enquiry">ENQUIRY NOW</span>
  </div>

  <div class="abs brand">
    <span class="brand-mark"></span>
    <span class="brand-name">Southern<br>Institute of<br>Applied<br>Skills</span>
  </div>

  <nav class="abs nav">
    <div class="nav-item" style="background:var(--nav-home)"><i></i>HOME</div>
    <div class="nav-item" style="background:var(--nav-about)"><i></i>ABOUT US</div>
    <div class="nav-item" style="background:var(--nav-courses)"><i></i>COURSES</div>
    <div class="nav-item" style="background:var(--nav-students)"><i></i>STUDENTS</div>
    <div class="nav-item" style="background:var(--nav-contact)"><i></i>CONTACT US</div>
  </nav>
</header>

<section>
  <div class="abs hero" role="img" aria-label="Photo of students looking at a phone together"></div>
  <svg class="abs" style="left:0;top:160px" width="708" height="26" viewBox="0 0 708 26">
    <path d="M0 16 C120 4 240 22 360 10 C480 0 600 14 708 6 L708 26 L0 26Z" fill="#fff" opacity=".45"/>
    <path d="M0 18 C140 12 260 26 380 18 C500 10 600 22 708 14 L708 26 L0 26Z" fill="#fff"/>
  </svg>
  <h1 class="abs hero-title">Our Courses</h1>
  <div class="abs crumb">HOME &nbsp;›&nbsp; COURSES</div>
</section>

<main>
  <!-- row 1 -->
  <article class="abs card" style="left:139px;top:228px">
    <div class="photo" role="img" aria-label="Photo of two colleagues discussing work at a laptop" style="background:linear-gradient(135deg,#3c3b38,#9a7a4a)"></div>
    <span class="cat">Business</span>
    <h2 class="title">Diploma of Leadership and Management</h2>
    <div class="meta"><b></b>BSB51918<s></s>10am - 12pm</div>
    <p class="desc">Business training program involve various aspects of managing scarce resources in a business entity and supporting a business</p>
    <span class="apply">APPLY NOW</span>
  </article>
  <article class="abs card" style="left:286px;top:228px">
    <div class="photo" role="img" aria-label="Photo of a café counter seen from above" style="background:linear-gradient(135deg,#3a2a20,#8a5a38)"></div>
    <span class="cat">Hospitality</span>
    <h2 class="title">Diploma of Hospitality Management</h2>
    <div class="meta"><b></b>SIT50416<s></s>10am - 12pm</div>
    <p class="desc">This qualification reflects the role of highly skilled senior operators who use a broad range of hospitality skills combined</p>
    <span class="apply">APPLY NOW</span>
  </article>
  <article class="abs card" style="left:433px;top:228px">
    <div class="photo" role="img" aria-label="Photo of a cook preparing drinks at a counter" style="background:linear-gradient(135deg,#8a9aa8,#4a3a48)"></div>
    <span class="cat">Hospitality</span>
    <h2 class="title">Certificate IV in Commercial Cookery</h2>
    <div class="meta"><b></b>SIT40516<s></s>10am - 12pm</div>
    <p class="desc">This qualification reflects the role of com-mercial cooks who have a supervisory or team leading role in the kitchen.</p>
    <span class="apply">APPLY NOW</span>
  </article>

  <!-- row 2 -->
  <article class="abs card" style="left:139px;top:448px">
    <div class="photo" role="img" aria-label="Photo of students working on laptops around a table" style="background:linear-gradient(135deg,#7a6a58,#b8a890)"></div>
    <span class="cat">Business</span>
    <h2 class="title">Diploma of Leadership and Management</h2>
    <div class="meta"><b></b>BSB51918<s></s>10am - 12pm</div>
    <p class="desc">Business training program involve various aspects of managing scarce resources in a business entity and supporting a business</p>
    <span class="apply">APPLY NOW</span>
  </article>
  <article class="abs card" style="left:286px;top:448px">
    <div class="photo" role="img" aria-label="Photo of a business team gathered around a laptop" style="background:linear-gradient(135deg,#2e2c2c,#7a6e66)"></div>
    <span class="cat">Hospitality</span>
    <h2 class="title">Diploma of Hospitality Management</h2>
    <div class="meta"><b></b>SIT50416<s></s>10am - 12pm</div>
    <p class="desc">This qualification reflects the role of highly skilled senior operators who use a broad range of hospitality skills combined</p>
    <span class="apply">APPLY NOW</span>
  </article>
  <article class="abs card" style="left:433px;top:448px">
    <div class="photo" role="img" aria-label="Photo of baristas behind a café counter with a chalkboard wall" style="background:linear-gradient(135deg,#5a6e66,#a89a88)"></div>
    <span class="cat">Hospitality</span>
    <h2 class="title">Certificate IV in Commercial Cookery</h2>
    <div class="meta"><b></b>SIT40516<s></s>10am - 12pm</div>
    <p class="desc">This qualification reflects the role of com-mercial cooks who have a supervisory or team leading role in the kitchen.</p>
    <span class="apply">APPLY NOW</span>
  </article>

  <!-- row 3 -->
  <article class="abs card" style="left:139px;top:667px">
    <div class="photo" role="img" aria-label="Photo of two students sharing a laptop" style="background:linear-gradient(135deg,#4a3a30,#8a7060)"></div>
    <span class="cat">Business</span>
    <h2 class="title">Diploma of Leadership and Management</h2>
    <div class="meta"><b></b>BSB51918<s></s>10am - 12pm</div>
    <p class="desc">Business training program involve various aspects of managing scarce resources in a business entity and supporting a business</p>
    <span class="apply">APPLY NOW</span>
  </article>
  <article class="abs card" style="left:286px;top:667px">
    <div class="photo" role="img" aria-label="Photo of a waiter serving a burger" style="background:linear-gradient(135deg,#3a2418,#9a3a2a)"></div>
    <span class="cat">Hospitality</span>
    <h2 class="title">Diploma of Hospitality Management</h2>
    <div class="meta"><b></b>SIT50416<s></s>10am - 12pm</div>
    <p class="desc">This qualification reflects the role of highly skilled senior operators who use a broad range of hospitality skills combined</p>
    <span class="apply">APPLY NOW</span>
  </article>
  <article class="abs card" style="left:433px;top:667px">
    <div class="photo" role="img" aria-label="Photo of a team meeting in a bright office" style="background:linear-gradient(135deg,#d8dadc,#8a8a8e)"></div>
    <span class="cat">Hospitality</span>
    <h2 class="title">Certificate IV in Commercial Cookery</h2>
    <div class="meta"><b></b>SIT40516<s></s>10am - 12pm</div>
    <p class="desc">This qualification reflects the role of com-mercial cooks who have a supervisory or team leading role in the kitchen.</p>
    <span class="apply">APPLY NOW</span>
  </article>

  <div class="abs load-more">LOAD MORE</div>
</main>

<footer>
  <svg class="abs footer-bg" width="708" height="246" viewBox="0 0 708 246">
    <path d="M0 0 L355 58 L708 0 L708 246 L0 246Z" fill="var(--navy)"/>
    <path d="M0 6 L333 50" stroke="#fff" stroke-width="2.5"/>
    <path d="M708 6 L378 50" stroke="#fff" stroke-width="2.5"/>
  </svg>
  <div class="abs footer-badge">SIAS</div>

  <div class="abs f-brand">
    <span class="brand-mark"></span>
    <span class="brand-name">Southern<br>Institute of<br>Applied<br>Skills</span>
  </div>
  <div class="abs f-contact" style="top:1066px"><i></i><span>18 Harrow Lane, Kingsford<br>ACT 2600</span></div>
  <div class="abs f-contact" style="top:1089px"><i></i><span>+61 400 555 012</span></div>
  <div class="abs f-contact" style="top:1105px"><i></i><span>info@sias.edu.au</span></div>
  <div class="abs f-contact" style="top:1120px"><i></i><span>Mon - Fri 8.30 AM - 04.30 PM</span></div>

  <div class="abs" style="left:249px;top:1025px">
    <div class="f-head">QUICK LINK</div>
    <ul class="f-list" style="margin-top:10px">
      <li>Home</li><li>About Us</li><li>Courses</li><li>Students</li><li>Contact Us</li>
    </ul>
  </div>
  <div class="abs" style="left:312px;top:1025px">
    <div class="f-head">COURSES</div>
    <ul class="f-list" style="margin-top:10px">
      <li>Diploma of Hospitality Management</li>
      <li>Diploma of Leadership and Management</li>
      <li>Certificate IV in Commercial Cookery</li>
    </ul>
  </div>

  <p class="abs f-news">Leave your details if you'd like to receive updates and news from us</p>
  <div class="abs f-input">Email Address
    <svg style="position:absolute;right:8px;top:6px" width="8" height="8" viewBox="0 0 8 8"><path d="M0 4 L8 0 L6 8 L4 5Z" fill="var(--red)"/></svg>
  </div>
  <span class="abs f-social" style="left:449px;top:1080px"></span>
  <span class="abs f-social" style="left:466px;top:1080px"></span>
  <span class="abs f-social" style="left:484px;top:1080px"></span>

  <div class="abs copyright">Copyright © 2019. Southern Institute of Applied Skills Pty Ltd | ACN: 600111222 | RTO: 90001.</div>
</footer>

</body>
</html>
```